Report Design Template Needed for Strategy Consulting Co.

I have a small consulting business that does market research, develops marketing strategy, and does business development work (sales, finding partners, preparing for investors) for small and medium-sized companies who can’t afford their own full-time marketing person.

Most of my reports are PowerPoint Decks. There is usually a Title Page, a Table of Contents, an Executive Summary, a Detailed Findings section (with some section breaks, so I need a divider page between sections), and a Recommendations section.

I need a report template/style that is attractive, professional and not too bold such that it takes away from the content, which is what they are paying for.

I have color palette ideas and graphics in the attached brief. Please let me know if you need anything else, or if you need graphic files.

Thank you!!

Target Market(s)

Small business professionals, scientists, business development executives.

Industry/Entity Type

Marketing

Font styles to use
Sans Serif

Requirements
Must have
• Should have the sections listed in the brief. Also, need to be able to import the template complete.
Should not have
• Background must not overtake the text

```html
<!DOCTYPE html>
<html lang="en">
<head>
<meta charset="utf-8">
<title>Report Template – Slide Overview</title>
<link href="https://fonts.googleapis.com/css2?family=Open+Sans:ital,wght@0,300;0,400;0,600;1,400&display=swap" rel="stylesheet">
<style>
  :root {
    --page: #ffffff;
    --sand: #e2ddcb;
    --stone: #8d8979;
    --stone-dark: #6f6b5d;
    --ink: #5e5b50;
    --blue: #1f6a92;
    --navy: #3e5566;
    --green: #93a83c;
    --sky: #9cbcdb;
    --link: #8aa6d1;
    --gutter: #c9c9c9;
  }
  * { box-sizing: border-box; margin: 0; padding: 0; }
  html, body { width: 1200px; height: 659px; overflow: hidden; background: var(--page); }
  body { position: relative; font-family: "Open Sans", Arial, sans-serif; }
  .spread-gutter {
    position: absolute; left: 586px; top: 0; width: 18px; height: 659px;
    background: linear-gradient(to right, #ffffff 0%, #e4e4e4 45%, var(--gutter) 55%, #f2f2f2 100%);
  }
  .slide {
    position: absolute; width: 231px; height: 130px;
    outline: 1px solid #b9b4a2;
    background: var(--sand);
    overflow: hidden;
  }
  .slide svg { display: block; width: 231px; height: 130px; }
  .col-a { left: 41px; } .col-b { left: 293px; }
  .col-c { left: 676px; } .col-d { left: 928px; }
  .row-1 { top: 34px; } .row-2 { top: 251px; } .row-3 { top: 468px; }
  .brand { font-family: "Open Sans", Arial, sans-serif; font-size: 4.6px; fill: var(--stone-dark); font-weight: 600; }
  .section-label { font-size: 6px; fill: var(--ink); }
  .title-main { font-size: 9.5px; fill: var(--ink); font-weight: 300; }
  .title-sub { font-size: 6px; fill: var(--stone); font-weight: 300; }
  .slide-heading { font-size: 8.5px; fill: var(--ink); }
  .page-no { font-size: 4.5px; fill: var(--stone); }
  .body-text { font-size: 4.2px; fill: var(--ink); }
  .body-link { fill: var(--link); }
  .chart-caption { font-size: 4.6px; fill: var(--ink); font-style: italic; }
  .tiny { font-size: 3.6px; fill: var(--ink); }
  .shape-line { fill: none; stroke: var(--stone); stroke-width: 1; }
  .shape-fill { fill: var(--stone); }
</style>
</head>
<body>

<svg width="0" height="0" style="position:absolute" aria-hidden="true">
  <defs>
    <symbol id="cover-panel" viewBox="0 0 231 130">
      <path d="M0 0 H90 Q99 60 102 130 H0 Z" fill="var(--stone)"/>
      <path d="M91 0 H97 Q106 60 108 130 H102 Q99 60 91 0 Z" fill="var(--blue)"/>
      <path d="M99 0 H103 Q112 60 114 130 H110 Q107 60 99 0 Z" fill="var(--green)"/>
    </symbol>
    <symbol id="content-edge" viewBox="0 0 231 130">
      <rect x="0" y="0" width="1.6" height="130" fill="var(--blue)"/>
      <rect x="2.2" y="0" width="1.4" height="130" fill="var(--green)"/>
    </symbol>
  </defs>
</svg>

<div class="spread-gutter"></div>

<!-- Title slide -->
<section class="slide col-a row-1" aria-label="Title slide">
  <svg viewBox="0 0 231 130">
    <use href="#cover-panel"/>
    <text class="title-main" x="222" y="79" text-anchor="end">Presentation title</text>
    <text class="title-sub" x="222" y="89" text-anchor="end">Prepared for Lorem ipsum</text>
    <text class="title-sub" x="222" y="100" text-anchor="end">Lorem ipsum</text>
    <text class="brand" x="226" y="124" text-anchor="end">Northfield Advisory</text>
  </svg>
</section>

<!-- Executive summary divider -->
<section class="slide col-b row-1" aria-label="Executive Summary divider">
  <svg viewBox="0 0 231 130">
    <use href="#cover-panel"/>
    <g class="shape-fill" transform="translate(173 22)">
      <rect x="-8" y="0" width="16" height="14" rx="4"/>
      <path d="M-12 16 H12 L4 40 L0 44 L-4 40 Z"/>
    </g>
    <circle cx="173" cy="46" r="2.2" fill="var(--sand)"/>
    <line x1="173" y1="48" x2="173" y2="64" stroke="var(--sand)" stroke-width="0.8"/>
    <text class="section-label" x="173" y="79" text-anchor="middle">Executive Summary</text>
    <text class="brand" x="226" y="124" text-anchor="end">Northfield Advisory</text>
  </svg>
</section>

<!-- Table of contents divider -->
<section class="slide col-a row-2" aria-label="Table of contents divider">
  <svg viewBox="0 0 231 130">
    <use href="#cover-panel"/>
    <rect x="160" y="38" width="26" height="30" class="shape-line" stroke-width="1.4"/>
    <g stroke="var(--stone)" stroke-width="1.2">
      <line x1="164" y1="44" x2="182" y2="44"/>
      <line x1="164" y1="49" x2="182" y2="49"/>
      <line x1="164" y1="54" x2="182" y2="54"/>
      <line x1="164" y1="59" x2="182" y2="59"/>
      <line x1="164" y1="64" x2="182" y2="64"/>
    </g>
    <text class="section-label" x="173" y="80" text-anchor="middle">Table of contents</text>
    <text class="brand" x="226" y="124" text-anchor="end">Northfield Advisory</text>
  </svg>
</section>

<!-- Detailed findings divider -->
<section class="slide col-b row-2" aria-label="Detailed Findings divider">
  <svg viewBox="0 0 231 130">
    <use href="#cover-panel"/>
    <path d="M152 58 Q173 36 194 58 Q173 80 152 58 Z" class="shape-fill"/>
    <circle cx="173" cy="57" r="8" fill="var(--sand)"/>
    <circle cx="173" cy="57" r="5" class="shape-fill"/>
    <text class="section-label" x="173" y="79" text-anchor="middle">Detailed Findings</text>
    <text class="brand" x="226" y="124" text-anchor="end">Northfield Advisory</text>
  </svg>
</section>

<!-- Recommendations divider -->
<section class="slide col-a row-3" aria-label="Recommendations divider">
  <svg viewBox="0 0 231 130">
    <use href="#cover-panel"/>
    <g class="shape-fill">
      <rect x="171" y="28" width="5" height="44" rx="1.5" transform="rotate(45 173.5 50)"/>
      <rect x="171" y="28" width="5" height="44" rx="1.5" transform="rotate(-45 173.5 50)"/>
      <rect x="152" y="28" width="14" height="8" rx="1" transform="rotate(-45 159 32)"/>
      <circle cx="189" cy="33" r="6"/>
    </g>
    <circle cx="191" cy="31" r="2.6" fill="var(--sand)"/>
    <text class="section-label" x="173" y="82" text-anchor="middle">Recommendations</text>
    <text class="brand" x="226" y="124" text-anchor="end">Northfield Advisory</text>
  </svg>
</section>

<!-- Content slide -->
<section class="slide col-b row-3" aria-label="Content slide with chart">
  <svg viewBox="0 0 231 130">
    <use href="#content-edge"/>
    <text class="slide-heading" x="7" y="11">Proin commodo convallis pulvinar</text>
    <text class="page-no" x="226" y="8" text-anchor="end">6</text>
    <g class="body-text">
      <circle cx="9" cy="34" r="0.8" fill="var(--stone)"/>
      <text x="12" y="35.5">Nullam interdum <tspan class="body-link">dignissim orci</tspan> ac blandit.</text>
      <circle cx="9" cy="42" r="0.8" fill="var(--stone)"/>
      <text x="12" y="43.5">Etiam convallis, ante ut aliquet congue, enim</text>
      <text x="12" y="48.5">ipsum varius justo, at pellentesque lectus libero</text>
      <text x="12" y="53.5">sed <tspan class="body-link">ipsum</tspan>.</text>
      <circle cx="9" cy="60" r="0.8" fill="var(--stone)"/>
      <text x="12" y="61.5">Cras lacus nisi, congue vel dui et, dictum</text>
      <text x="12" y="66.5" class="body-link">rhoncus massa.</text>
    </g>
    <path d="M36 71 H106 L71 78 Z" class="shape-fill"/>
    <text class="body-text" x="71" y="90" text-anchor="middle" font-size="5">Lorem <tspan class="body-link">ipsum</tspan> dolor sit amet</text>
    <line x1="145" y1="24" x2="145" y2="105" stroke="var(--stone)" stroke-width="0.5"/>
    <text class="chart-caption" x="187" y="25" text-anchor="middle">Lorem ipsum dolor (unit)</text>
    <g stroke="var(--stone)" stroke-width="0.4" fill="none">
      <line x1="158" y1="33" x2="158" y2="87"/>
      <line x1="158" y1="87" x2="222" y2="87"/>
    </g>
    <g fill="#b5b1a3" stroke="var(--stone)" stroke-width="0.4">
      <circle cx="200" cy="47" r="4.5"/>
      <circle cx="190" cy="52" r="3"/>
      <circle cx="177" cy="57" r="4"/>
      <circle cx="180" cy="64" r="2.2"/>
      <circle cx="163" cy="83" r="1.2"/>
    </g>
    <text class="brand" x="226" y="124" text-anchor="end">Northfield Advisory</text>
  </svg>
</section>

<!-- Image slide -->
<section class="slide col-c row-1" aria-label="Image slide">
  <svg viewBox="0 0 231 130">
    <defs>
      <linearGradient id="sheet-tone" x1="0" y1="0" x2="1" y2="1">
        <stop offset="0" stop-color="#f1f1f1"/>
        <stop offset="1" stop-color="#c8c8c8"/>
      </linearGradient>
    </defs>
    <rect x="0" y="0" width="231" height="130" fill="url(#sheet-tone)" role="img" aria-label="Sheet of decorative graphic elements: numerals, frames, arcs and chevrons"/>
    <text class="page-no" x="226" y="8" text-anchor="end">7</text>
    <rect x="141" y="89" width="90" height="18" fill="var(--stone)"/>
    <text x="148" y="100.5" font-size="6" fill="#f1efe6">Quisque nec varius elit.</text>
  </svg>
</section>

<!-- Palette slide -->
<section class="slide col-d row-1" aria-label="Colour palette slide">
  <svg viewBox="0 0 231 130">
    <text class="page-no" x="226" y="8" text-anchor="end">8</text>
    <rect x="50" y="28" width="87" height="45" rx="3" fill="none" stroke="#f3efe2" stroke-width="0.8"/>
    <g>
      <rect x="111" y="44" width="8" height="14" fill="#efebdd"/>
      <rect x="120" y="44" width="2" height="14" fill="#3f3f3f"/>
      <rect x="123" y="44" width="2" height="14" fill="#6f6f6f"/>
      <rect x="126" y="44" width="2" height="14" fill="#a7a7a7"/>
      <rect x="129" y="44" width="2" height="14" fill="#d8d8d8"/>
    </g>
    <g>
      <rect x="138" y="28" width="38" height="17" rx="2" fill="var(--blue)"/>
      <rect x="138" y="50" width="38" height="17" rx="2" fill="var(--green)"/>
      <rect x="138" y="72" width="38" height="17" rx="2" fill="var(--sky)"/>
      <rect x="50" y="72" width="38" height="17" rx="2" fill="var(--stone)"/>
      <rect x="94" y="72" width="38" height="17" rx="2" fill="var(--navy)"/>
    </g>
    <g fill="#e8ecef" opacity="0.85">
      <rect x="148" y="31" width="2" height="11"/><rect x="152" y="31" width="2" height="11"/><rect x="156" y="31" width="2" height="11"/><rect x="160" y="31" width="2" height="11"/>
      <rect x="148" y="53" width="2" height="11"/><rect x="152" y="53" width="2" height="11"/><rect x="156" y="53" width="2" height="11"/><rect x="160" y="53" width="2" height="11"/>
      <rect x="148" y="75" width="2" height="11"/><rect x="152" y="75" width="2" height="11"/><rect x="156" y="75" width="2" height="11"/><rect x="160" y="75" width="2" height="11"/>
      <rect x="60" y="75" width="2" height="11"/><rect x="64" y="75" width="2" height="11"/><rect x="68" y="75" width="2" height="11"/><rect x="72" y="75" width="2" height="11"/>
      <rect x="104" y="75" width="2" height="11"/><rect x="108" y="75" width="2" height="11"/><rect x="112" y="75" width="2" height="11"/><rect x="116" y="75" width="2" height="11"/>
    </g>
  </svg>
</section>

<!-- Concepts 1 -->
<section class="slide col-c row-2" aria-label="Concepts slide one">
  <svg viewBox="0 0 231 130">
    <text class="slide-heading" x="4" y="11">Concepts (1/3)</text>
    <g class="shape-fill">
      <path d="M4 30 H24 L28 35 L24 40 H4 Z"/>
      <path d="M26 30 H46 L50 35 L46 40 H26 L30 35 Z"/>
      <path d="M48 30 H68 L72 35 L68 40 H48 L52 35 Z"/>
      <path d="M90 30 H110 L114 35 L110 40 H90 Z"/>
      <path d="M112 30 H132 L136 35 L132 40 H112 L116 35 Z"/>
      <path d="M134 30 H154 L158 35 L154 40 H134 L138 35 Z"/>
    </g>
    <g class="tiny" fill="#f1efe6">
      <text x="30" y="36.5" fill="#f1efe6">XXX</text>
      <text x="54" y="36.5" fill="#f1efe6">XXX</text>
      <text x="93" y="28" fill="var(--ink)">XXX</text><text x="108" y="28" fill="var(--ink)">XXX</text><text x="123" y="28" fill="var(--ink)">XXX</text>
    </g>
    <g class="shape-line" stroke-width="0.7">
      <path d="M4 46 H54 L60 70 L54 98 H4 Z"/>
      <path d="M54 46 H134 V98 H54 L60 70 Z"/>
    </g>
    <g class="tiny">
      <text x="20" y="58">• XXX</text><text x="20" y="64">• XXX</text><text x="20" y="70">• XXX</text><text x="20" y="76">• XXX</text>
      <text x="66" y="58">• XXX</text><text x="66" y="64">• XXX</text><text x="66" y="70">• XXX</text><text x="66" y="76">• XXX</text>
    </g>
    <path d="M150 54 L164 78 H136 Z" class="shape-fill"/>
    <circle cx="150" cy="70" r="5" fill="var(--sand)"/>
    <g class="shape-line" stroke-width="1.3">
      <circle cx="143" cy="96" r="4"/><circle cx="158" cy="96" r="4"/>
      <line x1="147" y1="96" x2="154" y2="96"/>
    </g>
    <g class="shape-line" stroke-width="2">
      <path d="M183 36 A10 10 0 0 1 192 44"/>
      <path d="M192 50 A10 10 0 0 1 184 58"/>
      <path d="M178 58 A10 10 0 0 1 170 50"/>
      <path d="M170 44 A10 10 0 0 1 178 36"/>
    </g>
    <rect x="168" y="78" width="24" height="24" class="shape-fill"/>
    <rect x="170" y="80" width="9" height="9" fill="var(--sand)"/>
    <rect x="181" y="91" width="9" height="9" fill="var(--sand)"/>
  </svg>
</section>

<!-- Concepts 2 -->
<section class="slide col-d row-2" aria-label="Concepts slide two">
  <svg viewBox="0 0 231 130">
    <text class="slide-heading" x="4" y="11">Concepts (2/3)</text>
    <g class="shape-line" stroke-width="0.7">
      <path d="M4 24 H40 L48 34 V60 L40 72 H4 Z"/>
      <circle cx="70" cy="55" r="24"/>
      <path d="M100 34 L108 24 H132 V80 H108 L100 70 Z"/>
    </g>
    <g class="tiny">
      <text x="14" y="40">• XXX</text><text x="14" y="46">• XXX</text><text x="14" y="52">• XXX</text><text x="14" y="58">• XXX</text>
      <text x="65" y="57">XXX</text>
      <text x="112" y="46">• XXX</text><text x="112" y="52">• XXX</text><text x="112" y="58">• XXX</text><text x="112" y="64">• XXX</text>
    </g>
    <g class="shape-line" stroke-width="1">
      <circle cx="148" cy="48" r="13"/><circle cx="148" cy="48" r="9.5"/><circle cx="148" cy="48" r="6"/><circle cx="148" cy="48" r="2.5"/>
      <path d="M138 82 Q148 74 158 82"/><path d="M141 86 Q148 80 155 86"/>
    </g>
    <circle cx="148" cy="89" r="1.4" class="shape-fill"/>
    <g class="shape-fill">
      <path d="M174 48 L180 43 V53 Z"/><path d="M200 48 L194 43 V53 Z"/>
      <path d="M187 35 L182 41 H192 Z"/><path d="M187 61 L182 55 H192 Z"/>
      <rect x="179" y="47" width="16" height="2"/><rect x="186" y="40" width="2" height="16"/>
      <path d="M183 74 L189 71 L195 74 V81 L189 84 L183 81 Z"/>
      <path d="M176 86 L182 83 L188 86 V93 L182 96 L176 93 Z"/>
      <path d="M190 86 L196 83 L202 86 V93 L196 96 L190 93 Z"/>
      <path d="M20 98 H46 M46 98 L38 92 M46 98 L38 104" stroke="var(--stone)" stroke-width="1.6"/>
    </g>
  </svg>
</section>

<!-- Concepts 3 -->
<section class="slide col-c row-3" aria-label="Concepts slide three">
  <svg viewBox="0 0 231 130">
    <text class="slide-heading" x="4" y="11">Concepts (3/3)</text>
    <g class="shape-fill">
      <circle cx="38" cy="35" r="9"/><circle cx="24" cy="49" r="9"/><circle cx="52" cy="49" r="9"/><circle cx="38" cy="63" r="9"/>
      <circle cx="168" cy="38" r="10"/><circle cx="188" cy="38" r="10"/><circle cx="168" cy="58" r="10"/><circle cx="188" cy="58" r="10"/>
      <path d="M4 86 H38 L16 92 Z"/>
      <path d="M52 84 L60 96 L52 108 Z"/>
    </g>
    <g class="shape-line" stroke-width="0.6">
      <circle cx="38" cy="49" r="6"/>
      <circle cx="108" cy="41" r="4"/><circle cx="98" cy="56" r="3"/><circle cx="108" cy="58" r="3"/><circle cx="118" cy="56" r="3"/>
      <path d="M108 45 V55 M106 44 L99 53 M110 44 L117 53"/>
      <rect x="92" y="84" width="14" height="10"/><rect x="102" y="90" width="14" height="10"/><rect x="94" y="98" width="14" height="10"/><rect x="108" y="78" width="12" height="10"/>
    </g>
    <g>
      <circle cx="146" cy="89" r="6" class="shape-fill"/>
      <circle cx="160" cy="89" r="6" class="shape-fill"/><path d="M160 83 A6 6 0 0 1 166 89 H160 Z" fill="var(--sky)"/>
      <circle cx="174" cy="89" r="6" class="shape-fill"/><path d="M174 83 A6 6 0 0 1 174 95 Z" fill="var(--sky)"/>
      <circle cx="188" cy="89" r="6" fill="var(--sky)"/><path d="M188 83 A6 6 0 0 0 182 89 H188 Z" fill="var(--stone)"/>
      <circle cx="202" cy="89" r="6" fill="var(--sky)"/>
    </g>
  </svg>
</section>

</body>
</html>
```